KVRD Pinecrest Rehabilitation Consultants, INC
Business Card and Stationary for KVRD Pinecrest Rehabilitation
Professional
Dorian K. Lumbard, Ph. D.
Vocational Rehabilitation Consultant
4173b GA Hwy 508 STE 612 Conyers, GA 30081
Dorian.Lumbard@kvrdpinecrestrehab.example
www.kvrdpinecrestrehab.example
I will need whole set of stationary, letterhead, envelopes etc.

```html
<!DOCTYPE html>
<html lang="en">
<head>
<meta charset="utf-8">
<title>KVRD Pinecrest Rehabilitation – Business Card</title>
<link rel="stylesheet" href="https://fonts.googleapis.com/css2?family=Montserrat:wght@400;500;600;700&display=swap">
<style>
  :root{
    --page-bg:#e9ebee;
    --card-white:#ffffff;
    --card-grey:#e6e7e9;
    --brand-blue:#1f6fc0;
    --brand-blue-dark:#0f4f98;
    --brand-blue-light:#4aa3e6;
    --swoosh-dark:#2b2d31;
    --text-dark:#333840;
    --mark-grey:#5a5f66;
  }
  *{margin:0;padding:0;box-sizing:border-box}
  html,body{width:1200px;height:901px;overflow:hidden}
  body{background:var(--page-bg);font-family:"Montserrat",sans-serif;position:relative}
  .card{
    position:absolute;left:100px;top:165px;width:1000px;height:572px;
    border-radius:40px;overflow:hidden;
    background:linear-gradient(160deg,var(--card-white) 30%,var(--card-grey) 100%);
    box-shadow:0 18px 40px rgba(0,0,0,.18);
  }
  .card-swoosh{position:absolute;inset:0;width:100%;height:100%}
  .identity{position:absolute;left:70px;top:130px;width:380px;text-align:center}
  .brand-mark{
    width:150px;height:150px;border-radius:50%;
    background:var(--mark-grey);margin:0 auto 14px;
  }
  .brand-name{
    color:var(--brand-blue-dark);font-weight:500;font-size:58px;letter-spacing:6px;line-height:1;
  }
  .brand-sub{
    color:var(--brand-blue-dark);font-weight:500;font-size:14px;letter-spacing:3px;margin-top:8px;
  }
  .person-name{
    color:var(--brand-blue);font-weight:600;font-size:30px;letter-spacing:1px;margin-top:22px;text-align:left;padding-left:4px;
  }
  .person-title{color:var(--text-dark);font-size:22px;font-weight:500;text-align:left;padding-left:4px;margin-top:2px}
  .contact{
    position:absolute;right:60px;top:70px;width:330px;color:#fff;font-size:19px;
  }
  .contact-address{line-height:1.4;font-weight:500;margin-bottom:24px}
  .contact-line{display:flex;align-items:center;justify-content:flex-end;gap:14px;height:38px;font-weight:400}
  .contact-line svg{width:20px;height:20px;flex:none}
</style>
</head>
<body>
  <div class="card">
    <svg class="card-swoosh" viewBox="0 0 1000 572" preserveAspectRatio="none" aria-hidden="true">
      <path d="M520 0 C 500 250, 420 470, 250 572 L 300 572 C 470 470, 560 250, 585 0 Z" fill="var(--swoosh-dark)"/>
      <path d="M585 0 C 560 250, 470 470, 300 572 L 1000 572 L 1000 0 Z" fill="var(--brand-blue-light)"/>
      <path d="M605 0 C 585 250, 500 470, 335 572 L 1000 572 L 1000 0 Z" fill="var(--brand-blue)"/>
      <path d="M640 0 C 630 260, 560 460, 420 572 L 1000 572 L 1000 0 Z" fill="var(--brand-blue-dark)" opacity=".35"/>
    </svg>

    <div class="identity">
      <div class="brand-mark"></div>
      <div class="brand-name">KVRD</div>
      <div class="brand-sub">PINECREST REHABILITATION</div>
      <div class="person-name">MARCUS DELANEY</div>
      <div class="person-title">Managing Director</div>
    </div>

    <div class="contact">
      <p class="contact-address" style="text-align:right">217 9th Floor Plaza,<br>Harbor Road NKC</p>
      <p class="contact-line">014 382 5716
        <svg viewBox="0 0 24 24"><path d="M6.6 10.8a15 15 0 0 0 6.6 6.6l2.2-2.2c.3-.3.7-.4 1-.2 1.1.4 2.3.6 3.6.6.6 0 1 .4 1 1V20c0 .6-.4 1-1 1A17 17 0 0 1 3 4c0-.6.4-1 1-1h3.5c.6 0 1 .4 1 1 0 1.3.2 2.5.6 3.6.1.3 0 .7-.2 1z" fill="#fff"/></svg>
      </p>
      <p class="contact-line">014 382 5717
        <svg viewBox="0 0 24 24"><rect x="6" y="2" width="12" height="20" rx="2" fill="none" stroke="#fff" stroke-width="2"/><circle cx="12" cy="18" r="1.2" fill="#fff"/></svg>
      </p>
      <p class="contact-line">mail@kvrdpinecrest.example
        <svg viewBox="0 0 24 24"><rect x="2" y="5" width="20" height="14" rx="1.5" fill="none" stroke="#fff" stroke-width="2"/><path d="M3 6l9 7 9-7" fill="none" stroke="#fff" stroke-width="2"/></svg>
      </p>
      <p class="contact-line">www.kvrdpinecrest.example
        <svg viewBox="0 0 24 24"><circle cx="12" cy="12" r="9" fill="none" stroke="#fff" stroke-width="2"/><path d="M3 12h18M12 3c3 3 3 15 0 18M12 3c-3 3-3 15 0 18" fill="none" stroke="#fff" stroke-width="1.6"/></svg>
      </p>
    </div>
  </div>
</body>
</html>
```